Stationery design for Shuttles and Transfers company - PELICAN
Stationery design
Stationery design for Shuttles and Transfers company - PELICAN - Transportation
Creative Brief
Simple
Nomsa Dlakavu
Ms
17 Marwick Lane Fernhollow
n_dlakavu@mailorbit.example
17 Marwick Lane
I need an email signature designed as well
Offering a comprehensive transport solution for your little one's safety. Terrace Point Business Park 84 Ravelston Avenue Ext 13 Ground Floor Building No. 4 Johannesburg 2000 Tel +2711 902 4175 Email info@pelicanroutes.co.za Website www.pelicanroutes.co.za

```html
<!DOCTYPE html>
<html lang="en">
<head>
<meta charset="utf-8">
<title>Pelican Shuttles and Transfers – Business Card</title>
<link rel="stylesheet" href="https://fonts.googleapis.com/css2?family=Open+Sans:wght@400;600;700&display=swap">
<style>
  :root {
    --backdrop: #8c8c8c;
    --card-black: #050505;
    --gold-dark: #6a3d12;
    --gold-mid: #d4922f;
    --gold-deep: #8c5719;
    --gold-icon: #c98a2c;
    --white: #ffffff;
    --divider: #5a5a5a;
  }
  html, body {
    margin: 0;
    padding: 0;
    width: 1200px;
    height: 780px;
    overflow: hidden;
    background: var(--backdrop);
  }
  .canvas {
    width: 1200px;
    height: 780px;
    display: flex;
    align-items: center;
    justify-content: center;
  }
  .business-card {
    display: block;
    width: 1000px;
    height: 570px;
  }
  .card-text {
    font-family: "Open Sans", Arial, sans-serif;
    fill: var(--white);
  }
  .holder-name { font-size: 31px; font-weight: 700; }
  .holder-role { font-size: 21px; font-weight: 400; }
  .contact-line { font-size: 21px; font-weight: 400; }
  .brand-name { font-size: 58px; font-weight: 400; letter-spacing: 9px; }
  .contact-icon { fill: var(--gold-icon); }
  .contact-icon-stroke { fill: none; stroke: var(--gold-icon); stroke-width: 2; }
  .brand-ring { fill: none; stroke: var(--gold-mid); stroke-width: 3; }
</style>
</head>
<body>
<main class="canvas">
  <svg class="business-card" viewBox="0 0 1000 570" xmlns="http://www.w3.org/2000/svg" aria-label="Pelican business card for Nomsa Dlakavu, Director">
    <defs>
      <clipPath id="card-shape">
        <rect x="0" y="0" width="1000" height="570" rx="30" ry="30"/>
      </clipPath>
      <linearGradient id="gold-band" x1="0" y1="0" x2="1" y2="0.3">
        <stop offset="0" stop-color="var(--gold-dark)"/>
        <stop offset="0.45" stop-color="var(--gold-mid)"/>
        <stop offset="1" stop-color="var(--gold-deep)"/>
      </linearGradient>
      <linearGradient id="divider-fade" x1="0" y1="0" x2="0" y2="1">
        <stop offset="0" stop-color="var(--divider)" stop-opacity="0"/>
        <stop offset="0.4" stop-color="var(--divider)"/>
        <stop offset="1" stop-color="var(--divider)" stop-opacity="0"/>
      </linearGradient>
    </defs>

    <g clip-path="url(#card-shape)">
      <!-- gold header band -->
      <rect class="header-band" x="0" y="0" width="1000" height="570" fill="url(#gold-band)"/>
      <!-- thin dark accent stripe under the name -->
      <path class="header-accent" d="M560 215 C 700 190 860 160 1000 105 L1000 122 C 860 178 700 205 560 215 Z" fill="var(--card-black)"/>
      <!-- black body with wave edge -->
      <path class="card-body" d="M0 300 C 70 190 250 160 420 190 C 600 222 790 222 1000 140 L1000 570 L0 570 Z" fill="var(--card-black)"/>
      <!-- white swoosh -->
      <path class="white-swoosh" d="M0 500 C 10 330 130 240 330 210 C 170 250 60 330 34 500 Z" fill="var(--white)"/>
    </g>

    <!-- holder -->
    <text class="card-text holder-name" x="948" y="78" text-anchor="end">Nomsa Dlakavu</text>
    <text class="card-text holder-role" x="948" y="110" text-anchor="end">Director</text>

    <!-- brand block -->
    <circle class="brand-ring" cx="290" cy="345" r="56"/>
    <text class="card-text brand-name" x="295" y="470" text-anchor="middle">PELICAN</text>

    <!-- divider -->
    <rect class="column-divider" x="498" y="290" width="2" height="260" fill="url(#divider-fade)"/>

    <!-- contact details -->
    <text class="card-text contact-line" x="525" y="322">17 Marwick Lane</text>
    <text class="card-text contact-line" x="528" y="352">Fernhollow</text>

    <g class="icon-phone" transform="translate(533 384)">
      <rect class="contact-icon" x="0" y="7" width="20" height="12" rx="3"/>
      <path class="contact-icon" d="M-1 7 C 4 -1 16 -1 21 7 L16 8 L14 4 L6 4 L4 8 Z"/>
    </g>
    <text class="card-text contact-line" x="563" y="402">0736140957</text>

    <g class="icon-mobile" transform="translate(536 413)">
      <rect class="contact-icon-stroke" x="1" y="1" width="13" height="22" rx="2"/>
      <rect class="contact-icon" x="4" y="4" width="7" height="13"/>
    </g>
    <text class="card-text contact-line" x="563" y="432">+27736140957</text>

    <g class="icon-mail" transform="translate(533 448)">
      <rect class="contact-icon" x="0" y="0" width="20" height="14" rx="1"/>
      <path d="M1 1 L10 8 L19 1" fill="none" stroke="var(--card-black)" stroke-width="1.8"/>
    </g>
    <text class="card-text contact-line" x="563" y="462">n_dlakavu@mailorbit.example</text>

    <g class="icon-web" transform="translate(543 487)">
      <circle class="contact-icon" cx="0" cy="0" r="9"/>
      <ellipse cx="0" cy="0" rx="4" ry="9" fill="none" stroke="var(--card-black)" stroke-width="1.3"/>
      <line x1="-9" y1="0" x2="9" y2="0" stroke="var(--card-black)" stroke-width="1.3"/>
    </g>
    <text class="card-text contact-line" x="563" y="494">www.pelicanroutes.co.za</text>
  </svg>
</main>
</body>
</html>
```